Web Design Project - vR Advise

We want to modernise our web page profile. We have an existing web site that we are particularly not proud of (www.vradvise.com.au).
We have started to build a new web site using Joomla and we like the structure of it, but we need it to be professionally designed and implemented.

This current development site can be viewed here: dev.vradvise.com.au

We would like a complete design for the entire website, ready for deployment.

(We still need to finalise the content, as we have just developed new products that we hope to launch in August both on this web site and by a Vendor Forum.)
Updates

Target Market(s)

Larger companies where the robustness of their IT infrastructure is critical. Our tools and services provide for monitoring of every device

Industry/Entity Type

Build

Requirements
Must have
• Responsive design for different screen sizes.

BrightDock help desk software integrated with the website.
Currently can be viewed at support.vradvise.com.au
Brightdock only supports custom css.

Nice to have
• Customer experience testimonials in a rotating banner
Chirpr and Pagebook links in the footer
We use Avenir as a company font.
Use company colours as in the logo (green and blue)

```html
<!DOCTYPE html>
<html lang="en">
<head>
<meta charset="utf-8">
<title>vR Advise</title>
<link rel="stylesheet" href="https://fonts.googleapis.com/css2?family=Oswald:wght@400;500&family=Arimo:wght@400&display=swap">
<style>
:root{
  --green:#a6b819;
  --green-dark:#8a9a10;
  --blue:#3a5f99;
  --ink:#4a4a4a;
  --body:#555;
  --rule:#e2e2e2;
  --footer:#3a3a3a;
  --white:#fff;
}
*{margin:0;padding:0;box-sizing:border-box}
html,body{width:1021px;height:1200px;overflow:hidden;background:var(--white)}
body{position:relative;font-family:"Arimo",Arial,sans-serif;color:var(--body)}
.abs{position:absolute}
.display{font-family:"Oswald","Arial Narrow",sans-serif;font-weight:400;text-transform:uppercase;color:var(--ink)}

/* header */
.brand{left:100px;top:36px;font-family:"Oswald",sans-serif;font-size:24px;color:var(--ink);font-weight:400}
.nav{right:104px;top:42px;display:flex;gap:41px;font-size:13.5px}
.nav a{text-decoration:none;color:var(--ink)}
.nav a.is-active{color:var(--green-dark)}

/* hero */
.hero{left:0;top:94px;width:1021px;height:357px;background:linear-gradient(100deg,#5fa6e0 0%,#2f7fc7 35%,#1a5a9a 65%,#2d3c52 100%)}
.hero-title{left:105px;top:244px;font-size:28px;color:#16212e;letter-spacing:-.5px}
.hero-sub{left:105px;top:275px;font-size:17px;color:var(--white);letter-spacing:-.3px}
.hero-dots{left:490px;top:413px;display:flex;gap:4px}
.hero-dots span{width:8px;height:8px;border-radius:50%;background:rgba(60,60,60,.6)}

/* services */
.section-title{font-size:23px}
.services-title{left:0;width:1021px;top:462px;text-align:center}
.services-rule{left:247px;top:500px;width:528px;height:1px;background:var(--rule)}
.service{top:526px;width:255px;text-align:center}
.service-icon{width:62px;height:62px;margin:0 auto;border:2.5px solid var(--green);border-radius:50%;display:flex;align-items:center;justify-content:center}
.service-name{font-size:14px;margin-top:7px;padding-bottom:5px;border-bottom:1px solid var(--rule)}
.service-text{font-size:10.5px;line-height:12.5px;margin-top:8px;color:#666}
.btn{display:inline-block;background:var(--green);color:var(--white);font-family:"Oswald",sans-serif;text-transform:uppercase;font-size:13.5px;padding:3px 8px;line-height:20px;text-decoration:none}
.service .btn{margin-top:17px}

.divider{left:102px;width:817px;height:1px;background:var(--rule)}

/* welcome */
.h-welcome{left:102px;top:743px;font-size:18px}
.h-welcome em{font-style:normal;color:var(--green)}
.welcome-photo{left:102px;top:777px;width:244px;height:143px;background:linear-gradient(90deg,#1d3b5e,#6e9cc4 55%,#173a63)}
.welcome-text{left:357px;top:773px;width:280px;font-size:12px;line-height:15.4px;text-align:justify}
.welcome-text p+p{margin-top:15px}

.h-support{left:664px;top:743px;font-size:18px}
.support-lead{left:664px;top:773px;width:247px;font-size:10.5px;line-height:15.4px;color:#7d8a00;text-align:justify}
.support-text{left:664px;top:834px;width:247px;font-size:10.2px;line-height:15.4px;text-align:justify;color:#666}

/* clients */
.h-clients{left:102px;top:1004px;font-size:18px}
.clients{left:102px;top:1060px;width:817px;display:flex;justify-content:space-between;align-items:center}
.client{display:flex;align-items:center;gap:6px;font-family:"Arimo",sans-serif;font-size:21px;color:var(--blue)}

/* footer */
.footer{left:0;top:1137px;width:1021px;height:63px;background:var(--footer)}
.copyright{left:110px;top:1161px;font-size:10.5px;color:#eee}
.social{right:106px;top:1153px;display:flex;gap:12px;align-items:center}
.social a{display:flex;align-items:center;gap:5px;color:#eee;text-decoration:none;font-size:10.5px}
.social i{width:14px;height:14px;display:block}
</style>
</head>
<body>

<header>
  <div class="abs brand">vR Advise</div>
  <nav class="abs nav display">
    <a class="is-active" href="#">Home</a>
    <a href="#">Services</a>
    <a href="#">Support</a>
    <a href="#">Products</a>
    <a href="#">About us</a>
    <a href="#">Contact</a>
  </nav>
</header>

<section>
  <div class="abs hero" role="img" aria-label="Hand touching a glowing laptop icon surrounded by device icons on a blue background"></div>
  <h1 class="abs hero-title display">Any device, any platform, anywhere</h1>
  <p class="abs hero-sub display">Cross domain ,performance &amp; service level monitoring &amp; management</p>
  <div class="abs hero-dots"><span></span><span></span><span></span></div>
</section>

<section>
  <h2 class="abs display section-title services-title">Our services</h2>
  <div class="abs services-rule"></div>

  <div class="abs service" style="left:102px">
    <div class="service-icon">
      <svg width="34" height="24" viewBox="0 0 34 24" fill="#444"><circle cx="9" cy="6" r="4"/><circle cx="25" cy="6" r="4"/><circle cx="17" cy="7" r="4.5"/><path d="M1 22c0-6 4-9 8-9s8 3 8 9zM17 22c0-6 4-9 8-9s8 3 8 9z"/><path d="M9 24c0-7 4-10 8-10s8 3 8 10z"/></svg>
    </div>
    <h3 class="service-name display">Consulting services</h3>
    <p class="service-text">Sed ut perspiciatis unde omnis iste natus error sit volup-tatem accusantium doloremque laudantium, totam rem aperiam, eaque ipsa quae ab illo inventore</p>
    <a class="btn" href="#">Read more</a>
  </div>

  <div class="abs service" style="left:383px">
    <div class="service-icon">
      <svg width="40" height="40" viewBox="0 0 40 40" fill="#333"><circle cx="9" cy="8" r="3"/><circle cx="20" cy="6" r="3.2"/><circle cx="31" cy="8" r="3"/><rect x="6" y="12" width="6" height="20" rx="2"/><rect x="17" y="10" width="6" height="24" rx="2"/><rect x="28" y="12" width="6" height="20" rx="2"/></svg>
    </div>
    <h3 class="service-name display">Professional services</h3>
    <p class="service-text">Sed ut perspiciatis unde omnis iste natus error sit volup-tatem accusantium doloremque laudantium, totam rem aperiam, eaque ipsa quae ab illo inventore</p>
    <a class="btn" href="#">Read more</a>
  </div>

  <div class="abs service" style="left:664px">
    <div class="service-icon">
      <svg width="38" height="38" viewBox="0 0 38 38" fill="none" stroke="#444" stroke-width="3"><circle cx="14" cy="14" r="7"/><circle cx="14" cy="14" r="11" stroke-dasharray="4 4"/><circle cx="28" cy="27" r="4"/><circle cx="28" cy="27" r="7" stroke-dasharray="3 3"/></svg>
    </div>
    <h3 class="service-name display">Productised services</h3>
    <p class="service-text">Sed ut perspiciatis unde omnis iste natus error sit volup-tatem accusantium doloremque laudantium, totam rem aperiam, eaque ipsa quae ab illo inventore</p>
    <a class="btn" href="#">Read more</a>
  </div>
</section>

<div class="abs divider" style="top:724px"></div>

<section>
  <h2 class="abs display h-welcome">Welcome to <em>vR Advise</em></h2>
  <div class="abs welcome-photo" role="img" aria-label="Two professionals looking at a transparent touch screen showing the globe"></div>
  <div class="abs welcome-text">
    <p>We are an organisation that prides itself on attracting, employing, retaining and developing subject matter experts in the field of consulting, architecture and delivery.</p>
    <p>We employ the best to ensure that we deliver the best. Our extensive experience and expertise fuels the architecture and delivery practices, ensuring that what we propose to our customers we also deploy, manage and support.</p>
  </div>
  <a class="abs btn" style="left:102px;top:937px" href="#">Read more</a>

  <h2 class="abs display h-support">Our support</h2>
  <p class="abs support-lead">At vR Advise our customers and their needs are our first priority, followed closely by our drive to stay on the edge of the ever evolving technology.</p>
  <p class="abs support-text">We are a company with big aspirations and an agile team of young and experienced IT professionals. We have a growing catalog of products, that becomes part of our fabric. We use products from these vendors because they have been tested and trialed by us and we believe them to be the best in class.</p>
  <a class="abs btn" style="left:664px;top:937px" href="#">Read more</a>
</section>

<div class="abs divider" style="top:986px"></div>

<section>
  <h2 class="abs display h-clients">Recent work with some of our clients</h2>
  <div class="abs clients">
    <span class="client">Brindlefen</span>
    <span class="client">Corvally</span>
    <span class="client">Osmuth</span>
    <span class="client">Kestrawn Telecom</span>
    <span class="client">Yarrowind</span>
  </div>
</section>

<footer>
  <div class="abs footer"></div>
  <p class="abs copyright">© 2011-2013 vR Advise | All rights reserved.</p>
  <div class="abs social">
    <a href="#"><i style="background:#3b5ca8"></i>Pagebook</a>
    <a href="#"><i style="background:#1da1e0"></i>Chirpr</a>
    <a href="#"><i style="background:#c8232c"></i>Pinlane</a>
    <a href="#"><i style="background:#d8261f"></i>Viewtube</a>
    <a href="#"><i style="background:#d64a3a"></i>Circleplus</a>
  </div>
</footer>

</body>
</html>
```